Flyer for the Harvest of lanterns conference

Flyer design for an annual international conference called "MERIVAL 2017". This is a conference for young adults, so we hope to produce a design that is both professional and appealing to young people in general

We'd like the flyer to showcase the conference brand logo, and clearly highlight the key information to people who will read it.

Target Market(s)

Young people, young adults

Industry/Entity Type

Religious

Font styles to use
Sans Serif

Colors

Designer to choose colors to be used in the design.

Requirements
Must have
• - Should be only one page (Vertical or Horizontal).
• - the MERVAL logo and all the information found in the attached text file. This includes: Main topic: Your sons and daughters shall prophesy,
• Dates and time, location, contact information and everything that is in the attached text file.
Nice to have
• It would be nice to see samples where the white logo is used and another where the black one is used.
Should not have
• This is NOT a folded flyer, we will be sticking it on doors and public places. And we will be printing large simple to put on walls. So only one page with few words like an add (the words are in the attached file)

```html
<!DOCTYPE html>
<html lang="en">
<head>
<meta charset="utf-8">
<title>MERIVAL 2017 – Harvest of lanterns conference</title>
<link href="https://fonts.googleapis.com/css2?family=Cinzel:wght@400;700&family=Open+Sans:wght@400;600;700&display=swap" rel="stylesheet">
<style>
  :root{
    --backdrop:#a9a9a9;
    --paper:#ffffff;
    --wine:#5e0000;
    --wine-deep:#4a0000;
    --title-red:#6a0a00;
    --amber:#e8960f;
    --amber-soft:#f2b652;
    --gold:#f7c54a;
    --ink:#333333;
    --ink-soft:#444444;
    --chip:#fdeedd;
    --band:#efefef;
  }
  *{box-sizing:border-box;margin:0;padding:0}
  html,body{width:1200px;height:1200px;overflow:hidden}
  body{background:var(--backdrop);font-family:"Open Sans",Arial,sans-serif;position:relative}
  .flyer{position:absolute;left:190px;top:20px;width:820px;height:1160px;background:var(--paper);overflow:hidden}

  .hero{position:absolute;left:0;top:0;width:820px;height:482px}
  .hero-photo{position:absolute;inset:0;
    background:
      radial-gradient(ellipse 55% 35% at 50% 0%, #fff6c8 0%, rgba(255,230,140,0) 70%),
      radial-gradient(ellipse 30% 35% at 52% 78%, #6e1300 0%, rgba(110,19,0,0) 100%),
      linear-gradient(180deg,#f6c434 0%,#f0a526 28%,#e3841d 48%,#c4591a 64%,#8b2708 82%,var(--wine) 100%);}
  .hero-title{position:absolute;top:40px;width:100%;text-align:center;font-family:"Cinzel",Georgia,serif;font-weight:700;font-size:58px;color:var(--title-red);letter-spacing:1px}
  .hero-subtitle{position:absolute;top:112px;width:100%;text-align:center;font-family:"Cinzel",Georgia,serif;font-weight:700;font-size:31px;color:var(--title-red);letter-spacing:1px}
  .hero-tagline{position:absolute;top:435px;width:100%;text-align:center;font-family:"Cinzel",Georgia,serif;font-weight:400;font-size:22px;color:#fff;letter-spacing:.5px}

  .brand-box{position:absolute;left:45px;top:505px;width:731px;height:262px;border:1.5px solid #9b3b30;border-top:none;border-radius:0 0 16px 16px}
  .brand-box::before,.brand-box::after{content:"";position:absolute;top:0;width:2px;height:60px;background:linear-gradient(#fff,rgba(255,255,255,0))}
  .brand-box::before{left:-2px}.brand-box::after{right:-2px}
  .brand-mark{position:absolute;left:80px;top:640px;width:300px;display:flex;align-items:center;justify-content:center;gap:14px}
  .brand-dot{width:30px;height:30px;border-radius:50%;background:var(--amber)}
  .brand-name{font-family:"Open Sans",Arial,sans-serif;font-weight:700;font-size:40px;color:#111;letter-spacing:3px}

  .speakers{position:absolute;left:405px;top:500px}
  .speakers h2{font-family:"Cinzel",Georgia,serif;font-weight:400;font-size:31px;color:var(--amber);letter-spacing:.5px}
  .speaker-list{list-style:none;margin-top:12px}
  .speaker-list li{height:40px;line-height:40px;padding-left:8px;width:300px;font-weight:700;font-size:18px;color:var(--ink)}
  .speaker-list li:nth-child(odd){background:linear-gradient(90deg,var(--chip) 75%,rgba(253,238,221,0))}

  .info-row{position:absolute;left:0;width:820px;background:linear-gradient(180deg,#fff 0%,var(--band) 100%)}
  .info-row .icon{position:absolute;left:126px;width:30px;height:30px}
  .info-row .label{position:absolute;left:182px;font-weight:600;font-size:20px;color:var(--amber)}
  .info-row .value{position:absolute;left:324px;font-size:20px;line-height:24px;color:var(--ink-soft)}
  .row-date{top:767px;height:101px}
  .row-location{top:868px;height:106px}
  .row-room{top:974px;height:84px}

  .contact{position:absolute;left:0;top:1058px;width:820px;height:102px;background:var(--wine)}
  .contact-tab{position:absolute;left:0;top:0;width:224px;height:102px;background:var(--amber-soft);clip-path:polygon(0 0,100% 0,82% 100%,0 100%)}
  .contact-label{position:absolute;left:76px;top:18px;font-weight:700;font-size:25px;line-height:30px;color:var(--wine)}
  .contact-phone{position:absolute;left:224px;width:596px;top:14px;text-align:center;font-weight:700;font-size:27px;color:#fff;display:flex;justify-content:center;align-items:center;gap:14px}
  .contact-web{position:absolute;left:224px;width:596px;top:58px;text-align:center;font-size:16px;color:#fff}
</style>
</head>
<body>
<main class="flyer">
  <header class="hero">
    <div class="hero-photo" role="img" aria-label="Photo of a person meditating on a mountain peak above golden sunlit mountain ranges"></div>
    <h1 class="hero-title">MERIVAL 2017</h1>
    <p class="hero-subtitle">Harvest of lanterns Conference</p>
    <p class="hero-tagline">Your sons and daughters shall prophesy</p>
  </header>

  <div class="brand-box"></div>
  <div class="brand-mark"><span class="brand-dot"></span><span class="brand-name">MERVAL</span></div>

  <section class="speakers">
    <h2>Speakers:</h2>
    <ul class="speaker-list">
      <li>Prophet Lucien Maboko</li>
      <li>Bishop Samuel Ndolo</li>
      <li>Prophet Gabriel Oyo Mutamba</li>
      <li>Prophet Remi Kasongo</li>
      <li>Prophet Josue Bilanga</li>
    </ul>
  </section>

  <section class="info-row row-date">
    <svg class="icon" style="top:35px" viewBox="0 0 30 30" fill="none" stroke="#e8960f" stroke-width="1.5">
      <rect x="2" y="4" width="26" height="24" rx="1"/><line x1="2" y1="10" x2="28" y2="10"/>
      <line x1="8" y1="1" x2="8" y2="6"/><line x1="22" y1="1" x2="22" y2="6"/>
      <path d="M6 14h18M6 18h18M6 22h18M10 12v14M15 12v14M20 12v14"/>
    </svg>
    <span class="label" style="top:34px">Date:</span>
    <p class="value" style="top:34px">September 1st, 2nd and 3rd 2017<br>Start Time: 6:00PM</p>
  </section>

  <section class="info-row row-location">
    <svg class="icon" style="top:14px" viewBox="0 0 30 34" fill="none" stroke="#e8960f" stroke-width="1.5">
      <path d="M15 26C9 18 7 15 7 11a8 8 0 0 1 16 0c0 4-2 7-8 15z"/><circle cx="15" cy="11" r="3"/>
      <ellipse cx="15" cy="27" rx="13" ry="4"/>
    </svg>
    <span class="label" style="top:18px">Location:</span>
    <p class="value" style="top:16px">Harborview Lantern Hotel<br>412 Elmwood Avenue<br>Brookhaven, ME 04999 United States</p>
  </section>

  <section class="info-row row-room">
    <svg class="icon" style="top:24px" viewBox="0 0 30 30" fill="none" stroke="#e8960f" stroke-width="1.5">
      <rect x="2" y="8" width="26" height="20"/><rect x="8" y="2" width="14" height="6"/>
      <path d="M6 13h18M6 17h18M6 21h4M20 21h4"/><rect x="12" y="21" width="6" height="7"/>
    </svg>
    <span class="label" style="top:28px">Room:</span>
    <p class="value" style="top:28px">Cedar Hall Ballroom</p>
  </section>

  <footer class="contact">
    <div class="contact-tab"></div>
    <p class="contact-label">Contact<br>Info:</p>
    <p class="contact-phone">
      <svg width="34" height="26" viewBox="0 0 34 26" fill="#f2b652">
        <path d="M2 9C8 2 26 2 32 9l-2 4-6-2v-3c-4-2-10-2-14 0v3l-6 2z"/>
        <path d="M9 13h16l4 11H5z" fill="none" stroke="#f2b652" stroke-width="2.5"/>
        <circle cx="17" cy="18" r="3"/>
      </svg>
      +1 (555) 014 2280
    </p>
    <p class="contact-web">Email:hello@lanternfield.org - Website: http://merivalhub.org</p>
  </footer>
</main>
</body>
</html>
```